New Business Card Design Project

I need a meaningful new business card. Therefore, the website should convey growth, joy, uniqueness, workout and a bit of luxury.
Color scheme should be petrol, gold and matching colors.

```html
<!DOCTYPE html>
<html lang="en">
<head>
<meta charset="utf-8">
<title>Core Balance Studio – Business Card</title>
<link rel="stylesheet" href="https://fonts.googleapis.com/css2?family=Montserrat:wght@400;500&family=Great+Vibes&display=swap">
<style>
  :root {
    --stage: #2a2a2a;
    --card: #121212;
    --petrol: #14a89c;
    --petrol-deep: #0c6f68;
    --ink: #f2f2f2;
    --muted: #cfcfcf;
  }
  * { box-sizing: border-box; margin: 0; padding: 0; }
  html, body { width: 1200px; height: 900px; overflow: hidden; }
  body {
    background: radial-gradient(ellipse at 40% 35%, #333 0%, var(--stage) 60%, #222 100%);
    font-family: "Montserrat", Arial, sans-serif;
    color: var(--ink);
    position: relative;
  }
  .card {
    position: absolute;
    width: 600px;
    height: 345px;
    background: var(--card);
    border-radius: 22px;
    border-bottom: 10px solid var(--petrol);
    overflow: hidden;
    box-shadow: 0 18px 40px rgba(0,0,0,0.45);
  }
  .card--front { left: 40px; top: 60px; }
  .card--back { left: 560px; top: 470px; }

  .brand {
    display: flex;
    align-items: center;
    gap: 14px;
    color: var(--petrol);
    font-weight: 500;
    letter-spacing: 0.04em;
    white-space: nowrap;
  }
  .brand__dot {
    border-radius: 50%;
    background: var(--petrol);
    flex: none;
  }

  /* Front */
  .card--front .brand {
    position: absolute;
    left: 0; right: 0; top: 138px;
    justify-content: center;
    font-size: 34px;
  }
  .card--front .brand__dot { width: 22px; height: 22px; }
  .front-rule {
    position: absolute;
    left: 170px; right: 170px;
    height: 1px;
    background: var(--petrol-deep);
  }
  .front-rule--top { top: 118px; }
  .front-rule--bottom { top: 200px; }

  /* Back */
  .card--back .brand {
    position: absolute;
    left: 32px; top: 36px;
    font-size: 19px;
  }
  .card--back .brand__dot { width: 14px; height: 14px; }
  .accent-bar {
    position: absolute;
    right: 0; top: 26px;
    width: 16px; height: 46px;
    background: var(--petrol);
  }
  .holder {
    position: absolute;
    right: 36px; top: 24px;
    text-align: right;
  }
  .holder__name {
    font-family: "Great Vibes", cursive;
    font-size: 36px;
    color: var(--petrol);
    line-height: 1;
  }
  .holder__name span { color: var(--ink); }
  .holder__role {
    font-size: 13px;
    color: var(--muted);
    margin-top: 2px;
  }
  .figure-art {
    position: absolute;
    right: 20px; bottom: 0;
    width: 240px; height: 250px;
  }
  .address {
    position: absolute;
    left: 32px; top: 118px;
    font-size: 15px;
    line-height: 1.45;
  }
  .contacts {
    position: absolute;
    left: 32px; top: 206px;
    list-style: none;
    font-size: 14px;
    line-height: 1;
  }
  .contacts li {
    display: flex;
    align-items: center;
    gap: 12px;
    margin-bottom: 14px;
  }
  .contacts svg { width: 15px; height: 15px; flex: none; }
  .icon-fill { fill: var(--petrol); }
  .icon-stroke { fill: none; stroke: var(--petrol); stroke-width: 2; }
</style>
</head>
<body>

<section class="card card--front" aria-label="Card front">
  <span class="front-rule front-rule--top"></span>
  <div class="brand"><span class="brand__dot"></span>Core Balance Studio</div>
  <span class="front-rule front-rule--bottom"></span>
</section>

<section class="card card--back" aria-label="Card back">
  <span class="accent-bar"></span>
  <div class="brand"><span class="brand__dot"></span>Core Balance Studio</div>

  <div class="holder">
    <div class="holder__name">Nadia <span>Farrell</span></div>
    <div class="holder__role">Owner</div>
  </div>

  <svg class="figure-art" role="img" aria-label="Line illustration of a woman in a seated leg-raise pilates pose" viewBox="0 0 240 250">
    <defs>
      <radialGradient id="figureTone" cx="0.5" cy="0.65" r="0.55">
        <stop offset="0" stop-color="#14a89c" stop-opacity="0.45"/>
        <stop offset="0.6" stop-color="#0c6f68" stop-opacity="0.22"/>
        <stop offset="1" stop-color="#121212" stop-opacity="0"/>
      </radialGradient>
    </defs>
    <rect width="240" height="250" fill="url(#figureTone)"/>
  </svg>

  <p class="address">418 Linden Ave, #112<br>Brookfield, OH 43190</p>

  <ul class="contacts">
    <li>
      <svg viewBox="0 0 24 24"><path class="icon-fill" d="M6.6 10.8a15 15 0 0 0 6.6 6.6l2.2-2.2a1 1 0 0 1 1-.25 11.4 11.4 0 0 0 3.6.57 1 1 0 0 1 1 1V20a1 1 0 0 1-1 1A17 17 0 0 1 3 4a1 1 0 0 1 1-1h3.5a1 1 0 0 1 1 1c0 1.25.2 2.45.57 3.6a1 1 0 0 1-.25 1z"/></svg>
      0419276508
    </li>
    <li>
      <svg viewBox="0 0 24 24"><rect class="icon-stroke" x="3" y="5" width="18" height="14" rx="1"/><path class="icon-stroke" d="M3 6l9 7 9-7"/></svg>
      hello@corebalancestudio.com
    </li>
    <li>
      <svg viewBox="0 0 24 24"><circle class="icon-stroke" cx="12" cy="12" r="9"/><path class="icon-stroke" d="M3 12h18M12 3c3 3 3 15 0 18M12 3c-3 3-3 15 0 18"/></svg>
      www.corebalancestudio.com
    </li>
  </ul>
</section>

</body>
</html>
```